Stationery Design Project

Brivan-Holt Consultants is interim management company. We are specialized in finding the best Finance and IT consultants for our clients when they require additional resources on an interim basis for projects or special situations. We are flexible in our approach and we always seek to maximize the benefits for our clients as well as our consultants.

We are looking for a design of our letterhead, general stationery and business cards using the company name. The design will also be found on our coming web pages.
Updates

Please also create a logo for Brivan-Holt Consultants which expresses that we want to match the best finance and IT people to our customers projects

Target Market(s)

Larger and mid sized companies (all sectors), as well as highly skilled Finance & IT professionals/consultants

Industry/Entity Type

Business

Requirements
Must have
• Brivan-Holt Consultants
We are expecting that 'Brivan-Holt' will be on the first line and 'Consultants' on a second line.
Please also indicate style of the letters for our address/phone and mail details. Our current address is:
Tarnvoldgade 9,
2870 Kalsbro
Danmark
Mobile: +45 XX XX XX XX Mail: xx@brivan-holt.dk

```html
<!DOCTYPE html>
<html lang="en">
<head>
<meta charset="utf-8">
<title>Brivan-Holt Consultants – Stationery</title>
<link rel="stylesheet" href="https://fonts.googleapis.com/css2?family=Mulish:ital,wght@0,400;0,600;0,700;0,800;1,400&display=swap">
<style>
  :root {
    --slate: #3f5563;
    --sky: #89cbe2;
    --mist: #8ea6b5;
    --paper: #ffffff;
    --edge: #9fb1bf;
    --shadow: rgba(90, 110, 130, 0.45);
    --canvas: #ffffff;
  }
  * { box-sizing: border-box; margin: 0; padding: 0; }
  html, body { width: 1200px; height: 900px; overflow: hidden; background: var(--canvas); }
  body { position: relative; font-family: "Mulish", "Helvetica Neue", Arial, sans-serif; }

  .sheet, .card { position: absolute; box-shadow: 7px 7px 7px var(--shadow); }

  .letterhead { left: 128px; top: 76px; width: 517px; height: 710px; background: var(--paper); border: 1px solid var(--edge); }

  .wordmark { position: absolute; display: flex; align-items: center; gap: 8px; color: var(--slate); }
  .wordmark__square { width: 22px; height: 22px; background: var(--sky); flex: none; }
  .wordmark__text { display: flex; flex-direction: column; font-weight: 600; line-height: 1; }
  .wordmark__name { font-size: 23px; letter-spacing: 0.5px; }
  .wordmark__line { font-size: 9.5px; letter-spacing: 3.6px; margin-top: 3px; }
  .wordmark--light { color: var(--paper); }

  .letterhead .wordmark { right: 40px; top: 28px; }

  .letterhead__contact { position: absolute; right: 32px; top: 80px; text-align: center; font-style: italic; font-size: 9.5px; line-height: 14px; color: var(--mist); letter-spacing: 0.2px; }

  .letterhead__footer-mark { position: absolute; left: 236px; top: 665px; font-size: 10px; font-weight: 600; color: var(--slate); letter-spacing: 0.5px; }

  .card { width: 234px; height: 143px; }
  .card--front-dark { left: 669px; top: 118px; background: var(--slate); }
  .card--back-white { left: 800px; top: 254px; background: var(--paper); border: 1px solid var(--edge); }
  .card--front-white { left: 669px; top: 464px; background: var(--paper); border: 1px solid var(--edge); }
  .card--back-sky { left: 800px; top: 602px; background: var(--sky); }

  .card .wordmark { left: 26px; top: 52px; }

  .card__person { position: absolute; display: flex; flex-direction: column; align-items: flex-end; }
  .card__name { font-size: 11px; font-weight: 700; line-height: 12px; }
  .card__role { font-size: 6px; font-weight: 800; letter-spacing: 0.3px; line-height: 8px; }
  .card__details { position: absolute; font-style: italic; font-size: 7.5px; line-height: 10.2px; }

  .card--back-white .card__person { left: 69px; top: 38px; }
  .card--back-white .card__name { color: var(--sky); }
  .card--back-white .card__role { color: var(--slate); }
  .card--back-white .card__details { left: 69px; top: 64px; color: var(--slate); }

  .card--back-sky .card__person { left: 89px; top: 35px; }
  .card--back-sky .card__name { color: var(--slate); }
  .card--back-sky .card__role { color: var(--paper); }
  .card--back-sky .card__details { left: 89px; top: 62px; color: var(--slate); }
</style>
</head>
<body>

  <section class="sheet letterhead" aria-label="Letterhead">
    <div class="wordmark">
      <span class="wordmark__square"></span>
      <span class="wordmark__text">
        <span class="wordmark__name">BRIVAN-HOLT</span>
        <span class="wordmark__line">CONSULTANTS</span>
      </span>
    </div>
    <p class="letterhead__contact">
      Tarnvoldgade 9 &nbsp;.&nbsp; 2870 Kalsbro &nbsp;.&nbsp; Danmark<br>
      Mobile: +45 31 62 47 80 &nbsp;.&nbsp; Mail: MK@brivan-holt.dk
    </p>
    <span class="letterhead__footer-mark">Brivan-Holt</span>
  </section>

  <section class="card card--front-dark" aria-label="Business card front, dark">
    <div class="wordmark wordmark--light">
      <span class="wordmark__square"></span>
      <span class="wordmark__text">
        <span class="wordmark__name">BRIVAN-HOLT</span>
        <span class="wordmark__line">CONSULTANTS</span>
      </span>
    </div>
  </section>

  <section class="card card--back-white" aria-label="Business card back, white">
    <div class="card__person">
      <span class="card__name">Mads Kjeldgaard</span>
      <span class="card__role">DIRECTOR</span>
    </div>
    <p class="card__details">
      Tarnvoldgade 9,<br>
      2870 Kalsbro<br>
      Danmark<br>
      Mobile: +45 31 62 47 80<br>
      Mail: MK@brivan-holt.dk
    </p>
  </section>

  <section class="card card--front-white" aria-label="Business card front, white">
    <div class="wordmark">
      <span class="wordmark__square"></span>
      <span class="wordmark__text">
        <span class="wordmark__name">BRIVAN-HOLT</span>
        <span class="wordmark__line">CONSULTANTS</span>
      </span>
    </div>
  </section>

  <section class="card card--back-sky" aria-label="Business card back, blue">
    <div class="card__person">
      <span class="card__name">Mads Kjeldgaard</span>
      <span class="card__role">DIRECTOR</span>
    </div>
    <p class="card__details">
      Tarnvoldgade 9,<br>
      2870 Kalsbro<br>
      Danmark<br>
      Mobile: +45 31 62 47 80<br>
      Mail: MK@brivan-holt.dk
    </p>
  </section>

</body>
</html>
```